Hip Music Management Co. BIz Card

I have a logo (attached) the back side of the card should the full logo on the entire card- that's it. The front side of the card should show the logo somewhere, keeping with the 4 different shades of blue. The front side of the card can be a white background with logo and colored typeface for all info. Pretty simple.

Target Market(s)

I manage and produce a whole bunch of major label and indie artists.

Industry/Entity Type

Management

Contact Information for Business Card

Velmora Sound House (logo)
Dale Fornwick
President
www.velmorasoundhouse.com
dale@velmorasoundhouse.com
+1 310.555.7182
418 Willow Bend Lane
Ashgrove Falls, NY 10599

Requirements
Must have
• Entire logo on back side. White background on front- unless you provide something more interesting.
Nice to have
• On the front of the card if you choose a white backgound, if possible take my logo without the blue background (over white) that would be cool.

```html
<!DOCTYPE html>
<html lang="en">
<head>
<meta charset="utf-8">
<title>Velmora Sound House – Business Card</title>
<link rel="stylesheet" href="https://fonts.googleapis.com/css2?family=Cabin:wght@400;600&display=swap">
<style>
  :root {
    --page-bg: #d6d6d4;
    --card-navy: #1a1c4a;
    --brand-cyan: #2aa9df;
    --text-white: #ffffff;
  }
  * { margin: 0; padding: 0; box-sizing: border-box; }
  html, body {
    width: 1200px;
    height: 1000px;
    overflow: hidden;
  }
  body {
    background: var(--page-bg);
    font-family: "Cabin", sans-serif;
    position: relative;
  }
  .card {
    position: absolute;
    background: var(--card-navy);
    color: var(--text-white);
  }
  .card-back {
    left: 510px;
    top: 101px;
    width: 593px;
    height: 259px;
  }
  .card-back .brand-name {
    position: absolute;
    left: 0;
    right: 0;
    top: 128px;
    text-align: center;
    font-size: 44px;
    font-weight: 600;
    color: var(--brand-cyan);
    line-height: 1;
  }
  .card-front {
    left: 101px;
    top: 333px;
    width: 600px;
    height: 351px;
  }
  .card-front .brand-name {
    position: absolute;
    left: 27px;
    top: 24px;
    font-size: 22px;
    font-weight: 600;
    color: var(--brand-cyan);
    line-height: 1;
  }
  .person {
    position: absolute;
    left: 0;
    right: 0;
    top: 92px;
    padding-left: 0;
    text-align: center;
    transform: translateX(0);
  }
  .person-name {
    font-size: 28px;
    font-weight: 400;
    letter-spacing: 0.5px;
    text-transform: uppercase;
    line-height: 1.15;
  }
  .person-title {
    font-size: 20px;
    font-weight: 400;
    line-height: 1.3;
  }
  .contact-list {
    position: absolute;
    left: 28px;
    top: 208px;
    list-style: none;
  }
  .contact-item {
    display: flex;
    align-items: center;
    height: 30.5px;
    font-size: 20px;
    letter-spacing: 0.2px;
  }
  .contact-icon {
    width: 22px;
    height: 22px;
    margin-right: 17px;
    flex: none;
    fill: none;
    stroke: var(--brand-cyan);
    stroke-width: 1.6;
  }
  .contact-icon .solid { fill: var(--brand-cyan); stroke: none; }
</style>
</head>
<body>

  <section class="card card-back" aria-label="Card back">
    <p class="brand-name">Velmora Sound House</p>
  </section>

  <section class="card card-front" aria-label="Card front">
    <p class="brand-name">Velmora Sound House</p>

    <div class="person">
      <p class="person-name">Dale Fornwick</p>
      <p class="person-title">President</p>
    </div>

    <ul class="contact-list">
      <li class="contact-item">
        <svg class="contact-icon" viewBox="0 0 22 22" aria-hidden="true">
          <rect x="6" y="1.5" width="10" height="19" rx="1.5"/>
          <line x1="6" y1="16" x2="16" y2="16"/>
          <circle class="solid" cx="11" cy="18.2" r="1"/>
        </svg>
        +1 310.555.7182
      </li>
      <li class="contact-item">
        <svg class="contact-icon" viewBox="0 0 22 22" aria-hidden="true">
          <path d="M2 9 L11 3 L20 9 V19 H2 Z"/>
          <path d="M2 9 L11 15 L20 9"/>
          <path d="M2 19 L9 13.5 M20 19 L13 13.5"/>
        </svg>
        dale@velmorasoundhouse.com
      </li>
      <li class="contact-item">
        <svg class="contact-icon" viewBox="0 0 22 22" aria-hidden="true">
          <rect x="4" y="4" width="14" height="10" rx="1"/>
          <path d="M1 18 L4 14 H18 L21 18 Z"/>
        </svg>
        www.velmorasoundhouse.com
      </li>
      <li class="contact-item">
        <svg class="contact-icon" viewBox="0 0 22 22" aria-hidden="true">
          <path class="solid" d="M11 1 C7 1 4.5 4 4.5 7.5 C4.5 12 11 21 11 21 C11 21 17.5 12 17.5 7.5 C17.5 4 15 1 11 1 Z M11 5 A2.6 2.6 0 1 0 11.01 5 Z" fill-rule="evenodd"/>
        </svg>
        418 Willow Bend Lane Ashgrove Falls, NY 10599
      </li>
    </ul>
  </section>

</body>
</html>
```